New look and feel for investment website

Hi

Our website needs a crisp and professional look and feel applying to it. Here’s the address: http://www.brightplinth.co.uk. Since posting the brief yesterday (Tuesday, 16 August), we've reduced the amount of content on the home page, which should make life a little easier for you. We will come back later today, with some points of reference in terms of sites we like the look of. (See below)

17 August, 1.20pm GMT. OK, comments generally on the designs submitted so far. Please keep in mind that images of graphs, piles of coins, paper money and pretty females are not what is required. Better to think in terms of abstract imagery instead. Ratios? Circles? Relationships? Patterns? Not money,sex,graphs etc. Hope that helps.

For guidance on look and feel, please refer to these sites, which we like:

http://www.morvelle.co.uk/
http://www.qz.com/
https://www.harrowfieldtamsin.com
https://www.pirelconcerns.com
https://www.kvantule.com
Updates

Here's the Tall Beacons logo created in AI CS5.

Our market is professional financial advisers and relatively sophisticated private investors. The look and feel therefore should be slick and sophisticated - not 'lively' and lightweight, more like a banking site. Please read the brief again where we've added a list of websites that we really like the look of to get a better feel for what we're looking for. Thanks once again, we appreciate the work you're putting in.

It's essential that all the elements that are on the current home page be included on all new designs. 

We use a device in our e-mails which you may wish to incorporate in your design.

Target Market(s)

Professional financial advisers. People who know about investment and money.

Industry/Entity Type

Investment

Requirements
Should not have
• Graphs or people.

```html
<!DOCTYPE html>
<html lang="en">
<head>
<meta charset="utf-8">
<title>Tall Beacons – Home</title>
<link href="https://fonts.googleapis.com/css2?family=Questrial&family=Open+Sans:wght@400;700&family=Gelasio:wght@400&display=swap" rel="stylesheet">
<style>
:root{
  --orange:#f7a33b;
  --orange-deep:#e98a17;
  --orange-text:#c9620d;
  --rust:#b8460b;
  --grey-logo:#5b5b5b;
  --cream:#f6f1ea;
  --panel:#fed9a2;
  --panel-light:#fff3e2;
  --red:#e21414;
  --red-dark:#c20000;
  --ink:#222;
  --brown:#3f2107;
  --line:#b58a5c;
}
*{margin:0;padding:0;box-sizing:border-box}
html,body{width:1074px;height:1200px;overflow:hidden;background:var(--cream)}
.page{position:relative;width:1004px;height:1122px;transform:scale(1.0697);transform-origin:0 0;background:var(--cream);font-family:"Open Sans",sans-serif;color:var(--ink)}
.abs{position:absolute}
.topline{left:0;top:0;width:1004px;height:3px;background:var(--orange)}
.header{left:0;top:3px;width:1004px;height:115px;background:#fff}
.brand{left:55px;top:30px;font-family:"Open Sans",sans-serif;font-weight:400;font-size:52px;line-height:64px;color:var(--grey-logo);letter-spacing:-1px}
.tagline{left:407px;top:45px;width:550px;font-family:"Questrial",sans-serif;font-size:14px;line-height:18px;color:var(--orange-deep)}
.tagline b{font-weight:700}
.band{left:0;top:118px;width:1004px;height:34px;background:repeating-linear-gradient(135deg,#fff 0 2px,#eee 2px 4px)}
.tab{top:122px;width:104px;height:30px;border-radius:8px 8px 0 0;background:linear-gradient(#fbc073,var(--orange-deep));color:#fff;font:700 12.5px "Open Sans",sans-serif;text-align:center;line-height:32px;text-decoration:none}
.baseline{left:0;top:152px;width:1004px;height:4px;background:var(--orange)}
.key-art{left:108px;top:156px;width:76px;height:124px;background:linear-gradient(160deg,#e2e2e2,#8d8d8d);border-radius:30px 30px 8px 8px}
.login{left:301px;top:166px;width:648px;height:105px;background:var(--panel);border:2px solid var(--orange);border-radius:6px}
.login h2{position:absolute;left:26px;top:10px;font:400 19px "Open Sans",sans-serif;color:#111}
.login label{position:absolute;top:44px;font-size:10.5px;color:#222}
.field{position:absolute;top:41px;height:21px;background:var(--panel-light);font-size:8.5px;color:#666;line-height:21px;padding-left:14px}
.btn-login{position:absolute;left:577px;top:40px;width:50px;height:23px;background:#fff;border:1px solid #bbb;font-size:10.5px;text-align:center;line-height:21px}
.login .member{position:absolute;left:28px;top:73px;font-size:12.5px;color:#333}
.login .member a{color:#9a2c06;text-decoration:none;margin-left:18px}
.nav{left:55px;top:288px;width:193px;list-style:none;font-family:"Questrial",sans-serif}
.nav li{border-bottom:1px dotted var(--orange);padding:6px 0 5px 19px;font-size:12.5px;color:var(--rust);position:relative;line-height:15px;min-height:28px}
.nav li::before{content:"→";position:absolute;left:0;font-size:10px;color:#333}
.nav li.current{font-weight:700;color:#a31d05}
.cta{left:52px;top:654px;width:194px;height:71px;border-radius:7px;background:linear-gradient(var(--red),var(--red-dark));border:1px solid #a00;color:#fff;font:400 16px "Questrial",sans-serif;text-align:center;line-height:70px;letter-spacing:.5px}
.notice{left:52px;top:740px;width:194px;height:140px;border:1px solid #d2451c;background:#fff;padding:4px 6px;font-size:11.5px;line-height:14.4px;color:var(--orange-text);text-align:justify;letter-spacing:.5px}
.notice b{color:#a53300}
.divider{top:282px;height:758px;border-left:1px dotted var(--line)}
.main{left:302px;top:298px;width:428px;font-size:11.5px;line-height:16px;letter-spacing:.45px;word-spacing:.5px;text-align:justify;color:#222}
.main h3{font:400 19.5px/24px "Gelasio",serif;color:var(--orange-text);margin:0 0 8px;text-align:left;letter-spacing:0;word-spacing:0}
.main h3.lead{color:#c05a0c;margin-top:16px}
.main p{margin-bottom:14px}
.main .brandword{color:var(--red);font-weight:700}
.main .aside-h{font:400 20.5px/26px "Gelasio",serif;color:var(--red);text-align:left;letter-spacing:0;word-spacing:0}
.main .aside-h small{font-size:14px;color:#555}
.strategy{left:312px;top:981px;width:400px;height:24px;border-radius:5px;background:linear-gradient(#ee2a2a,#c80000);border:1px solid #900;color:#fff;font:400 14px "Gelasio",serif;text-align:center;line-height:22px}
.side-intro{left:750px;top:306px;width:175px;font-size:12.5px;line-height:15px}
.stat{left:748px;width:198px;height:64px;border:1px solid var(--orange);border-radius:7px;background:linear-gradient(#fff,#fed9a8);padding:0 10px;display:flex;align-items:center;font-size:11px;line-height:13.5px;color:var(--orange-text);letter-spacing:.2px}
.footer{left:0;top:1043px;width:1004px;height:79px;background:var(--brown)}
.foot-links{left:52px;top:1066px;font:700 11.5px "Open Sans",sans-serif;color:#fff;letter-spacing:.3px}
.foot-links span{margin:0 5px}
.copy{left:52px;top:1097px;font-size:10px;color:#b4610e}
.follow{left:722px;top:1069px;font:700 11px "Open Sans",sans-serif;color:#fff;letter-spacing:.5px}
.social{top:1058px;width:32px;height:32px;border-radius:3px}
</style>
</head>
<body>
<div class="page">
  <div class="abs topline"></div>
  <header class="abs header"></header>
  <div class="abs brand">TallBeacons</div>
  <p class="abs tagline">A potential return of <b>23.57 %</b> a year from America's biggest businesses with the emphasis firmly on capital preservation. (OK: we know you've yet to learn to love it, so that's why you can use our service free of charge for six months!)</p>
  <div class="abs band"></div>
  <a class="abs tab" style="left:507px">Home</a>
  <a class="abs tab" style="left:620px">Free Register</a>
  <a class="abs tab" style="left:734px">Contact Us</a>
  <a class="abs tab" style="left:848px">Terms</a>
  <div class="abs baseline"></div>

  <div class="abs key-art" role="img" aria-label="Silver key on a ring"></div>

  <section class="abs login">
    <h2>User Login</h2>
    <label style="left:26px">User Name:</label>
    <div class="field" style="left:89px;width:197px">enter your user name</div>
    <label style="left:307px">Password:</label>
    <div class="field" style="left:361px;width:197px">xxxxxxxxxx</div>
    <div class="btn-login">login</div>
    <p class="member">Not yet a Member? <a>Register Free</a></p>
  </section>

  <ul class="abs nav">
    <li class="current">Home</li>
    <li>Two Minute Guide</li>
    <li>Current &amp; year to date</li>
    <li>performance</li>
    <li>Watch list</li>
    <li>Other key numbers</li>
    <li>Back tested results</li>
    <li>History of all trades</li>
    <li>FAQs</li>
    <li>About our analyses</li>
    <li>About value investing</li>
    <li style="border-bottom:none">The Broadline 1000 and the Meridian 500 index</li>
  </ul>

  <div class="abs cta">FREE REGISTER</div>
  <div class="abs notice"><b>We're not asking you to part company with any money — at least not right now.</b> All we need from you at the moment is your e-mail address then you'll be able to view our portfolio and Watch list for 6 months free of charge!</div>

  <div class="abs divider" style="left:268px"></div>
  <div class="abs divider" style="left:737px"></div>

  <main class="abs main">
    <h3>Something different...</h3>
    <p>You may well be thinking that <span class="brandword">Tall Beacons</span> is just another one of those banal share recommendation sites sprinkled with the usual idiotic and patronising platitudes, gross exaggerations, silly get-rich-quick promises and all the other stuff and nonsense you associate with the black art of share-tipping...</p>
    <h3 class="lead">Well, we have a pleasant surprise for you: you couldn't be further from the truth.</h3>
    <h3 style="color:#b9520a;margin-top:18px">No! No! No!</h3>
    <p>There's no newsletter to read, books to study, dvds to watch or traders' secrets to be revealed. No never-ending stream of recommendations. No webcasts. No effort or time to invest. No training. No research. No tedious market commentaries. And no financial discomfort for you whatsoever. (At least for the first six months that is!)</p>
    <h3 style="margin-top:22px">We don't get it right every time...</h3>
    <p>We do however, get it right 75.58 % of the time (the total of all our winning trades out of all our trades) and on that basis our portfolio should produce an average return of 23.57 % a year for you.</p>
    <h3 style="margin-top:20px">An average of five trades a year and never more than five holdings.</h3>
    <p style="margin-bottom:4px">We tested different numbers of holdings and capital allocation percentages. The best results came from a portfolio of no more than five holdings with the same amount of capital allocated to each holding. 20% per stock, in a portfolio comprised of no more than five investments. That's it. You don't have to do it that way, but it works for us.</p>
    <p class="aside-h">For a succinct explanation of our service and the results to date...<small>please go here</small></p>
  </main>
  <div class="abs strategy">More about the strategy we use to choose stocks...</div>

  <p class="abs side-intro">To use our service free of charge for six months, please go here...</p>
  <div class="abs stat" style="top:361px">Average, annualised compound return over to : 23.57 %</div>
  <div class="abs stat" style="top:437px">So far this year, the portfolio's return is 13.49 %</div>
  <div class="abs stat" style="top:511px">Worst ever annual loss: -1.48 %; best ever annual gain: 69.77 %</div>
  <div class="abs stat" style="top:587px">Average return per trade including losing trades:24.44%</div>
  <div class="abs stat" style="top:663px">Maximum number of winning/losing trades in a row: 11/4.</div>
  <div class="abs stat" style="top:739px">Average number of days a stock stays in the portfolio: 287</div>
  <div class="abs stat" style="top:815px">An average of five trades a year and never more than five holdings at any one time.</div>
  <div class="abs stat" style="top:892px">86 trades in total, of which 65 were profitable - a success rate of 75.58 %</div>

  <footer class="abs footer"></footer>
  <p class="abs foot-links">Login <span>|</span> Register for free <span>|</span> Contact us <span>|</span> Terms &amp; Conditions <span>|</span></p>
  <p class="abs copy">© Copyright Tall Beacons. All Rights Reserved</p>
  <p class="abs follow">FOLLOW ON US</p>
  <div class="abs social" style="left:827px;background:#3b5998"></div>
  <div class="abs social" style="left:875px;background:#5fc4ea"></div>
  <div class="abs social" style="left:920px;background:#1f7bb6"></div>
</div>
</body>
</html>
```